Neighbor of existing customer door hanger

We are a landscaping services company (Pest Control & Lawn Fertilization). I am looking for a piece that my sales people can leave behind at the neighbors of our current customers offering our services to them.

I'm not a graphics guy, not even close, I started making a sample that is not any good, but it might give the general idea. I have attached that design here. There is a template available from the printer for 4.25 x 11". I have included that as well

Target Market(s)

Women homeowners 35-50

Industry/Entity Type

Landscape Gardening

Font styles to use
Sans Serif

Colors

Designer to choose colors to be used in the design.

Requirements
Must have
• we are looking for a space to write the name or address of our customer, include 2 specials ( 1 for pest control, 1 for Lawn fertilization and weed control) that make the neighbors feel like they are getting a deal because they are neighbors of our customer.
• the back side of the postcard will list our range of services and have a space for the salesman to write his name.
• This will be printed on a glossy cardstock (unless the designer suggests something else).
• Phone numbers, Website, logos

```html
<!DOCTYPE html>
<html lang="en">
<head>
<meta charset="utf-8">
<title>Fairbrook Neighbor Door Hanger</title>
<link href="https://fonts.googleapis.com/css2?family=Montserrat:wght@300;400;500;600;700;800&family=Libre+Baskerville:ital,wght@0,400;0,700;1,400&display=swap" rel="stylesheet">
<style>
  :root{
    --backdrop:#d9dbdc;
    --card:#ffffff;
    --ink:#2f4a48;
    --slate:#6d8d92;
    --dark:#1b1b1b;
    --body:#444a4c;
    --brand:#1f9a3f;
    --gold:#f4c01e;
  }
  *{margin:0;padding:0;box-sizing:border-box}
  html,body{width:960px;height:1200px;overflow:hidden;background:var(--backdrop)}
  body{position:relative;font-family:"Montserrat",sans-serif;color:var(--dark)}
  .hanger{position:absolute;top:50px;width:424px;height:1080px;background:var(--card);overflow:hidden;box-shadow:0 4px 14px rgba(0,0,0,.18)}
  .hanger--front{left:44px}
  .hanger--back{left:492px;background:linear-gradient(180deg,#f6f7f7 0%,#eef0f0 40%,#f3f4f4 100%)}
  .hanger-hole{position:absolute;left:154px;top:46px;width:116px;height:116px;border-radius:50%;background:var(--backdrop);z-index:5}
  .hero-photo{position:absolute;left:0;top:0;width:424px;height:596px;
    background:linear-gradient(180deg,#4f9fd6 0%,#9cc9e6 30%,#cfd9d6 48%,#b9b39a 60%,#6f6a58 75%,#3f3b33 100%)}
  .lower-photo{position:absolute;left:0;top:596px;width:424px;height:484px;
    background:linear-gradient(180deg,#f2f3f3 0%,#e4e6e6 55%,#eef0f0 100%)}
  .hello{position:absolute;left:46px;top:170px;font-size:46px;line-height:48px;font-weight:600;letter-spacing:37px;color:var(--ink)}
  .city{position:absolute;left:44px;top:222px;font-size:28px;line-height:34px;font-weight:700;letter-spacing:7.8px;color:var(--slate)}
  .neighbors{position:absolute;left:46px;top:321px;font-size:28px;line-height:34px;font-weight:800;letter-spacing:8.5px;color:var(--ink)}
  .friends-frame{position:absolute;left:0;top:0}
  .friends-we{position:absolute;left:46px;top:462px;font-size:32px;line-height:32px;font-weight:700;letter-spacing:6px;color:#fff;white-space:nowrap}
  .friends-your{position:absolute;left:46px;top:503px;font-size:32px;line-height:32px;font-weight:700;letter-spacing:6px;color:#fff}
  .friends-big{position:absolute;left:170px;top:502px;font-size:44px;line-height:44px;font-weight:800;letter-spacing:-.5px;color:#fff}
  .write-in{position:absolute;left:50px;top:567px;width:324px;height:64px;background:#fff;border-radius:32px;border:1px solid #cfd2d2;box-shadow:0 2px 4px rgba(0,0,0,.12)}
  .neighbor-note{position:absolute;left:0;top:642px;width:424px;text-align:center;font-family:"Libre Baskerville",serif;font-style:italic;font-size:18px;line-height:23px;color:var(--body)}
  .cut-line{position:absolute;left:0;width:424px;height:0;border-top:3px dashed var(--dark)}
  .offer{position:absolute;left:38px}
  .offer-kicker{font-size:15px;font-weight:400;line-height:17px}
  .offer-title{font-size:26px;font-weight:800;line-height:26px}
  .offer-title--stack{font-size:20px;line-height:21px}
  .offer-sub{font-family:"Libre Baskerville",serif;font-style:italic;font-size:11px;margin-top:8px}
  .price-seal{position:absolute;width:128px;height:128px;border-radius:50%;background:var(--gold);box-shadow:0 2px 5px rgba(0,0,0,.3)}
  .price-seal svg{position:absolute;left:0;top:0}
  .price-text{position:absolute;left:0;top:0;width:128px;height:128px;transform:rotate(-28deg);text-align:center;font-family:"Libre Baskerville",serif;color:var(--dark)}
  .price-only{position:absolute;left:0;width:128px;top:26px;font-family:"Montserrat",sans-serif;font-weight:700;font-size:12px}
  .price-amount{position:absolute;left:0;width:128px;top:40px;font-weight:700;font-size:32px}
  .price-note{position:absolute;left:0;width:128px;top:82px;font-style:italic;font-size:12px}
  .brand-name{position:absolute;left:0;top:947px;width:424px;height:34px;line-height:34px;text-align:center;font-size:28px;font-weight:700;color:var(--brand);letter-spacing:1px}
  .brand-name i{display:inline-block;width:14px;height:14px;background:var(--brand);margin-left:10px;vertical-align:2px}
  .phone{position:absolute;left:0;top:992px;width:424px;line-height:30px;text-align:center;font-size:25px;font-weight:800;color:var(--brand)}
  .web{position:absolute;left:0;top:1016px;width:424px;line-height:20px;text-align:center;font-family:"Libre Baskerville",serif;font-style:italic;font-size:16px;color:var(--brand)}
  .years-over,.years-label{position:absolute;left:0;width:424px;text-align:center;font-size:28px;font-weight:700;letter-spacing:6px;color:var(--slate)}
  .years-over{top:174px}
  .years-label{top:292px}
  .years-number{position:absolute;left:0;top:196px;width:424px;text-align:center;font-size:96px;font-weight:600;color:var(--ink);line-height:110px}
  .family-note{position:absolute;left:0;top:334px;width:424px;text-align:center;font-family:"Libre Baskerville",serif;font-style:italic;font-size:18px;line-height:23px;color:var(--body)}
  .services-title{position:absolute;left:0;top:403px;width:424px;text-align:center;font-size:22px;font-weight:700;color:var(--body)}
  .services-list{position:absolute;left:0;top:432px;width:424px;list-style:none;text-align:center;font-size:15.5px;font-weight:300;line-height:19.4px;color:var(--body)}
  .sign-line{position:absolute;left:64px;top:842px;width:296px;border-top:2px dotted var(--body)}
  .sign-label{position:absolute;left:0;top:853px;width:424px;text-align:center;font-family:"Libre Baskerville",serif;font-style:italic;font-size:18px;color:var(--body)}
</style>
</head>
<body>

<section class="hanger hanger--front">
  <div class="hero-photo" role="img" aria-label="Aerial photo of Salt Lake City at sunrise with mountains and valley haze"></div>
  <div class="lower-photo" role="img" aria-label="Faded photo of a suburban house front"></div>
  <div class="hanger-hole"></div>

  <div class="hello">HELLO</div>
  <div class="city">SALT LAKE CITY</div>
  <div class="neighbors">NEIGHBORS</div>

  <svg class="friends-frame" width="424" height="600" viewBox="0 0 424 600" aria-hidden="true">
    <path d="M29.5 538 V457.5 H394.5 V538" fill="none" stroke="#fff" stroke-width="3"/>
    <path d="M28 536.5 H164" fill="none" stroke="#fff" stroke-width="3"/>
    <path d="M382 536.5 H396" fill="none" stroke="#fff" stroke-width="3"/>
  </svg>
  <div class="friends-we">WE SERVICE</div>
  <div class="friends-your">YOUR</div>
  <div class="friends-big">FRIENDS</div>

  <div class="write-in" aria-label="Space to write customer name or address"></div>

  <p class="neighbor-note">Because your friends use our services,<br>You get Neighborhood discounts!</p>

  <div class="cut-line" style="top:718px"></div>
  <div class="offer" style="top:734px">
    <div class="offer-kicker">Full Service</div>
    <div class="offer-title">PEST CONTROL</div>
    <div class="offer-sub">You won't see a bug or we retreat for FREE</div>
  </div>
  <div class="cut-line" style="top:814px"></div>
  <div class="offer" style="top:836px">
    <div class="offer-title offer-title--stack">LAWN FERTILIZATION<br>&amp; WEED CONTROL</div>
    <div class="offer-sub" style="margin-top:4px">Thick Green Grass and No Weeds</div>
  </div>
  <div class="cut-line" style="top:911px"></div>

  <div class="price-seal" style="left:268px;top:694px">
    <svg width="128" height="128" viewBox="0 0 128 128"><circle cx="64" cy="64" r="56" fill="none" stroke="#1b1b1b" stroke-width="1.2"/></svg>
    <div class="price-text"><span class="price-only">ONLY</span><span class="price-amount">$9.95</span><span class="price-note">First Service</span></div>
  </div>
  <div class="price-seal" style="left:268px;top:806px">
    <svg width="128" height="128" viewBox="0 0 128 128"><circle cx="64" cy="64" r="56" fill="none" stroke="#1b1b1b" stroke-width="1.2"/></svg>
    <div class="price-text"><span class="price-only">ONLY</span><span class="price-amount">$9.95</span><span class="price-note">First Service</span></div>
  </div>

  <div class="brand-name">Fairbrook<i></i></div>
  <div class="phone">801-555-0142</div>
  <div class="web">www.getfairbrook.com</div>
</section>

<section class="hanger hanger--back">
  <div class="lower-photo" style="top:0;height:1080px;opacity:.55" role="img" aria-label="Faint photo of a house exterior"></div>
  <div class="hanger-hole"></div>

  <div class="years-over">OVER</div>
  <div class="years-number">25</div>
  <div class="years-label">YEARS</div>
  <p class="family-note">Family Owned Business<br>Operated in Salt Lake Side</p>

  <h2 class="services-title">Our List of Services</h2>
  <ul class="services-list">
    <li>Full Service Pest Control</li>
    <li>Inside &amp; Out Treatments</li>
    <li>Wasps/Hornets</li>
    <li>Mice/Rats</li>
    <li>Gophers/Voles</li>
    <li>Lawn Fertilization &amp; Weed Control</li>
    <li>Sprinkler Repairs &amp; Installation</li>
    <li>Wiring</li>
    <li>Xeriscape/Drip Conversion</li>
    <li>Landscape Design &amp; Install</li>
    <li>Pavers</li>
    <li>Pergolas/Pavilions</li>
    <li>Retaining walls</li>
    <li>Steel retaining</li>
    <li>Water features</li>
    <li>Landscape Lighting</li>
    <li>Fire features</li>
  </ul>

  <div class="sign-line"></div>
  <div class="sign-label">Authorised Salesman</div>

  <div class="brand-name">Fairbrook<i></i></div>
  <div class="phone">801-555-0142</div>
  <div class="web">www.getfairbrook.com</div>
</section>

</body>
</html>
```